Hair salon Business Card

Beauty Salon
I would like to see designs using sky blue and a soft orange. Mainly I would like my name ( Glow N' Wave Salon ) used as the design

Industry/Entity Type

Business

Contact Information for Business Card

Glow N'Wave Salon
418 E Birchfield Hyw #14
San Dimas, Ca 91748
909 527-6184

```html
<!DOCTYPE html>
<html lang="en">
<head>
<meta charset="utf-8">
<title>Glow N'Wave Salon – Business Card</title>
<link rel="stylesheet" href="https://fonts.googleapis.com/css2?family=Open+Sans:wght@300;400;700&display=swap">
<style>
  :root {
    --page-bg: #ffffff;
    --sky: #a2eefc;
    --orange: #fdbd00;
    --white: #ffffff;
  }
  html, body {
    margin: 0;
    padding: 0;
    width: 1200px;
    height: 1000px;
    overflow: hidden;
    background: var(--page-bg);
  }
  .canvas {
    position: relative;
    width: 1200px;
    height: 1000px;
  }
  .business-card {
    position: absolute;
    left: 283px;
    top: 309px;
    width: 632px;
    height: 381px;
    overflow: hidden;
    background: var(--sky);
    font-family: "Open Sans", Arial, sans-serif;
  }
  .card-shapes {
    position: absolute;
    inset: 0;
  }
  .brand-mark {
    position: absolute;
    left: 30px;
    top: 150px;
    width: 180px;
    margin: 0;
    text-align: center;
    color: var(--white);
    font-weight: 700;
    font-size: 27px;
    line-height: 1.15;
  }
  .contact-block {
    position: absolute;
    left: 233px;
    top: 128px;
    width: 400px;
    text-align: center;
    color: var(--white);
  }
  .salon-name {
    margin: 0;
    font-weight: 700;
    font-size: 34px;
    line-height: 44px;
    letter-spacing: -0.2px;
  }
  .address-line {
    margin: 0;
    font-weight: 400;
    font-size: 23px;
    line-height: 32px;
  }
  .phone {
    margin: 0;
    font-weight: 700;
    font-size: 23px;
    line-height: 32px;
  }
</style>
</head>
<body>
  <main class="canvas">
    <section class="business-card" aria-label="Glow N'Wave Salon business card">
      <svg class="card-shapes" width="632" height="381" viewBox="0 0 632 381" aria-hidden="true">
        <circle class="arc-highlight" cx="471" cy="206" r="247" fill="var(--white)"/>
        <circle class="orange-disc" cx="495" cy="191" r="248" fill="var(--orange)"/>
      </svg>

      <p class="brand-mark">Glow N'Wave<br>Salon</p>

      <div class="contact-block">
        <h1 class="salon-name">Glow N'Wave Salon</h1>
        <p class="address-line">418 E Birchfield Hyw #14</p>
        <p class="address-line">San Dimas, Ca 91748</p>
        <p class="phone">909 527-6184</p>
      </div>
    </section>
  </main>
</body>
</html>
```